■依頼の目的/概要
ハルカゼのlumoraで電子書籍出版をします。

■本の内容
40代女性で話すことや伝えること
自分に自信はないけれど

起業したい、
夢や目標を叶えたい、
という方がターゲットです。

声と潜在意識(心)の力を使う「ひだまりトーン」で
人前で自信をもって伝えられるようになったり
やりたいことがどんどん実現できるようになる方法を
書きました。

声や潜在意識を使ったトレーニング、
実例を用いてお伝えしています。

■デザイン要望
40代女性が好むデザインが希望です。
顔写真も入れていただけたらと思います。
その際、手に持っている音符などは載せないようお願いいたします。

お写真と、電子書籍の文章をお送りいたします。

ご応募、心よりお待ちしております!!!

その他何かご不明な点がございましたら、お気軽にご質問下さい。
よろしくお願いいたします。
タイトルは
響きの名手がひもとく
輝く毎日をつくる心の整え方・磨き方
~ひだまりトーンの秘密~

著者は
ひだまりトーンコンサルタント
さとうれな

どうぞよろしくお願いいたします。
LQS表記では、表紙画像のサイズは 50 MB 未満表紙フ
ァイルの理想的な寸法は 2,560 x 1,600 ピクセルとなっています。

文字が見やすいこと。
女性的な優しいイメージと内容が合うもの、
という視点で選ばせていただきました。

素晴らしい作品ばかりで
選ばせていただくのに時間がかかりました。

短期間にも関わらず
素敵な作品を沢山ご応募いただき
どうもありがとうございました!

心より感謝いたします。

機会がございましたら
またどうぞよろしくお願いいたします。

```html
<!DOCTYPE html>
<html lang="ja">
<head>
<meta charset="utf-8">
<title>ひだまりトーンの秘密</title>
<link rel="stylesheet" href="https://fonts.googleapis.com/css2?family=Noto+Serif+JP:wght@500;700;900&family=Noto+Sans+JP:wght@500;700&display=swap">
<style>
  :root {
    --paper: #fffdfb;
    --ink: #3b3634;
    --brown: #7b5c40;
    --rose: #df6a86;
    --rose-soft: #ec8fa3;
    --honey: #f2c46c;
    --white: #ffffff;
    --photo-a: #f1dcd3;
    --photo-b: #c9a897;
    --figure-a: #fbe9de;
    --figure-b: #f2cfc0;
  }
  * { margin: 0; padding: 0; box-sizing: border-box; }
  html, body { width: 754px; height: 1200px; overflow: hidden; background: var(--paper); }
  .cover {
    position: relative; width: 754px; height: 1200px; overflow: hidden;
    background: var(--paper); color: var(--ink);
    font-family: "Noto Serif JP", serif;
  }
  .tagline {
    position: absolute; top: 26px; left: 0; width: 100%;
    text-align: center; font-size: 46px; font-weight: 700; color: var(--brown);
    letter-spacing: 2px;
  }
  .tagline-rule {
    position: absolute; top: 94px; left: 60px; width: 634px; height: 3px; background: var(--brown);
  }
  .title-line {
    position: absolute; font-weight: 900; line-height: 1; color: var(--ink); white-space: nowrap;
  }
  .title-line.l1 { top: 132px; left: 70px; font-size: 96px; }
  .title-line.l2 { top: 292px; left: 213px; font-size: 116px; }
  .title-line.l3 { top: 500px; left: 70px; font-size: 124px; }
  .author-photo {
    position: absolute; top: 158px; left: 462px; width: 160px; height: 160px; border-radius: 50%;
    background: radial-gradient(circle at 50% 40%, var(--photo-a), var(--photo-b));
    border: 6px solid var(--rose-soft);
  }
  .author {
    position: absolute; top: 255px; left: 18px; display: flex; align-items: baseline; gap: 10px;
    font-family: "Noto Sans JP", sans-serif; color: var(--ink);
  }
  .author-role { font-size: 17px; font-weight: 500; }
  .author-name { font-size: 32px; font-weight: 700; font-family: "Noto Serif JP", serif; }
  .author-mark { font-size: 17px; }
  .bubble { position: absolute; }
  .bubble.pink { top: 318px; left: 42px; }
  .bubble.yellow { top: 630px; left: 122px; }
  .figure {
    position: absolute; top: 420px; left: 440px; width: 280px; height: 360px;
    border-radius: 140px 140px 30px 30px;
    background: linear-gradient(180deg, var(--figure-a), var(--figure-b));
  }
  .band {
    position: absolute; left: 0; top: 855px; width: 754px; height: 345px; background: var(--rose);
  }
  .band-lead {
    position: absolute; left: 52px; font-size: 96px; font-weight: 900; color: var(--white); line-height: 1;
  }
  .band-lead.first { top: 880px; }
  .band-lead.second { top: 1010px; }
  .band-particle {
    position: absolute; top: 1040px; left: 256px; font-size: 24px; font-weight: 700;
    color: var(--white); writing-mode: vertical-rl; letter-spacing: 2px;
  }
  .promise {
    position: absolute; top: 880px; left: 318px; width: 410px; height: 298px;
    background: var(--white); border-radius: 22px; text-align: center; color: var(--rose);
  }
  .promise-label { margin-top: 16px; font-size: 34px; font-weight: 700; }
  .promise-line { font-size: 88px; font-weight: 900; line-height: 1.1; }
</style>
</head>
<body>
<div class="cover">
  <p class="tagline">響きの名手がひもとく</p>
  <div class="tagline-rule"></div>

  <div class="author-photo" role="img" aria-label="著者さとうれなの顔写真"></div>

  <h1>
    <span class="title-line l1">ひだまり</span>
    <span class="title-line l2">トーン</span>
    <span class="title-line l3">の秘密</span>
  </h1>

  <p class="author">
    <span class="author-role">ひだまりトーンコンサルタント</span>
    <span class="author-name">さとうれな</span>
    <span class="author-mark">[著]</span>
  </p>

  <svg class="bubble pink" width="110" height="115" viewBox="0 0 110 115" aria-hidden="true">
    <path d="M55 5a50 50 0 1 1-30 90l-18 15 6-25A50 50 0 0 1 55 5z" fill="var(--rose-soft)"/>
    <path d="M60 35v32" stroke="#fff" stroke-width="4"/>
    <ellipse cx="53" cy="68" rx="9" ry="7" fill="#fff"/>
    <path d="M60 35q10 6 14 14" stroke="#fff" stroke-width="4" fill="none"/>
  </svg>

  <svg class="bubble yellow" width="120" height="125" viewBox="0 0 120 125" aria-hidden="true">
    <path d="M60 5a55 55 0 1 1-34 98l-20 16 8-28A55 55 0 0 1 60 5z" fill="var(--honey)"/>
    <path d="M50 42l26-6v32M50 42v34" stroke="#fff" stroke-width="4" fill="none"/>
    <ellipse cx="44" cy="77" rx="8" ry="6" fill="#fff"/>
    <ellipse cx="70" cy="69" rx="8" ry="6" fill="#fff"/>
  </svg>

  <div class="figure" role="img" aria-label="手を広げてほほえむ女性のイラスト"></div>

  <div class="band"></div>
  <p class="band-lead first">輝く</p>
  <p class="band-lead second">毎日</p>
  <p class="band-particle">をつくる</p>

  <div class="promise">
    <p class="promise-label">\ 心の /</p>
    <p class="promise-line">整え方</p>
    <p class="promise-line">磨き方</p>
  </div>
</div>
</body>
</html>
```